Silver Willow Housekeeping Voro

I am looking for a car wrap design. I do not want to wrap the whole car. Id like to wrap the sides, some on the back and the hood. I am uploading a general idea of what im looking for. I’d prefer more white space than less. I’d like it to be fun without being funny or gimmicky. Back window can have some writing on it. In the examples I shared, I like the simplicity of them. It is a 2011 Voro Maltez.

Target Market(s)

Families. We give back time to enjoy life

Industry/Entity Type

Residential cleaning

Font styles to use
Sans Serif

Colors
0054AA
0677BA
7BADD7
CADEEF
E8F1F8
E54698
E96AAD
F1A4CE
F9D9EA
FCEFF6

Requirements
Must have
• Please ck website www.silverwillowhousekeeping.com for content and ideas. I’d like whatever is on the good to be backwards.
Should not have
• No charicaturest or cartoony stuff

```html
<!DOCTYPE html>
<html lang="en">
<head>
<meta charset="utf-8">
<title>Silver Willow Housekeeping – Vehicle Side Wrap</title>
<link rel="stylesheet" href="https://fonts.googleapis.com/css2?family=Poppins:wght@500;600;700&display=swap">
<style>
  :root {
    --blue-bright: #1a1fd6;
    --blue-deep: #0054AA;
    --pink: #E54698;
    --pink-soft: #E96AAD;
    --white: #ffffff;
  }
  html, body {
    margin: 0;
    padding: 0;
    width: 1200px;
    height: 1200px;
    overflow: hidden;
    background: var(--white);
  }
  .wrap-panel {
    position: relative;
    width: 1200px;
    height: 1200px;
    font-family: "Poppins", sans-serif;
  }
  .wrap-graphics {
    position: absolute;
    inset: 0;
  }
  .brand {
    position: absolute;
    left: 350px;
    top: 578px;
    display: flex;
    align-items: center;
    gap: 10px;
  }
  .brand-square {
    width: 54px;
    height: 54px;
    background: var(--pink);
    flex: none;
  }
  .brand-name {
    margin: 0;
    color: var(--blue-bright);
    font-weight: 700;
    font-size: 25px;
    line-height: 1.05;
  }
  .brand-tagline {
    margin: 2px 0 0;
    color: var(--pink);
    font-weight: 500;
    font-size: 13px;
    line-height: 1.2;
  }
  .services {
    position: absolute;
    left: 655px;
    top: 578px;
    width: 220px;
    margin: 0;
    padding: 0;
    list-style: none;
    display: flex;
    flex-wrap: wrap;
    justify-content: center;
    gap: 0 10px;
    color: var(--blue-bright);
    font-weight: 700;
    font-size: 16px;
    line-height: 1.35;
  }
  .services li::before {
    content: "";
    display: inline-block;
    width: 7px;
    height: 7px;
    margin-right: 4px;
    border-radius: 50%;
    background: var(--pink);
    vertical-align: middle;
  }
  .phone {
    position: absolute;
    left: 918px;
    top: 520px;
    margin: 0;
    color: var(--blue-bright);
    font-weight: 700;
    font-size: 25px;
    letter-spacing: 2px;
  }
  .website {
    position: absolute;
    left: 406px;
    top: 676px;
    margin: 0;
    color: var(--white);
    font-weight: 600;
    font-size: 17px;
    transform: rotate(-2deg);
    transform-origin: left center;
  }
</style>
</head>
<body>
  <main class="wrap-panel">
    <svg class="wrap-graphics" width="1200" height="1200" viewBox="0 0 1200 1200" aria-hidden="true">
      <path class="accent-line" d="M331 666 Q600 662 840 636" fill="none" stroke="var(--pink)" stroke-width="3"/>
      <path class="accent-swoosh" d="M800 642 Q960 597 1150 572 L1150 593 Q970 610 830 642 Z" fill="var(--pink)"/>
      <path class="base-band" d="M335 678 Q760 692 1150 600 L1150 662 Q760 762 335 718 Z" fill="var(--blue-bright)"/>
    </svg>

    <p class="phone">610-555-0187</p>

    <div class="brand">
      <span class="brand-square"></span>
      <div>
        <h1 class="brand-name">Silver Willow<br>Housekeeping</h1>
        <p class="brand-tagline">more time for your family</p>
      </div>
    </div>

    <ul class="services">
      <li>Disinfecting</li>
      <li>Cleaning</li>
      <li>House keeping</li>
    </ul>

    <p class="website">www.silverwillowhousekeeping.com</p>
  </main>
</body>
</html>
```